Website design for headhunting agency

The design I need (PSD file) is for a company offering specialised services in recruitment of high-end executive and management positions for businesses.
OBJECTIVES OF THE WEBSITE:
1. Let entrepreneurs and business leaders know about their services and easily have them contact Varolinq if they want more information about their services.
2. Display a list of available carreer opportunities (according to their client's need).
WHAT I NEED:
1st, I need the design for the Home Page ONLY. Once approved, I will need the other pages designed as well. (Here is prototype that we've already developed for the Website that will guide you in the design:
http://demo.pelvarshop.net/varolinq/fr/accueil)
ATTACHED FILES
- Logo
- PDF brochure: Use for inspiration. It is encouraged that you use pictures from this brochure. You can always suggest new ones, as long as they are not expensive to buy and have the same look and feel as the brochure.
HOMEPAGE:
1. Main menu : 6 sections
Accueil | Varolinq | Équipe | Approche | Postes disponibles | Publications
2. Main slider: 4 sections
- Chasseurs de têtes (Headhunters)
- Notre approche (Our Approach)
- Postes cadres disponibles (Executive Careers
Opportunities)
- Contactez-nous (Contact Us)
3. Main Call To Action Boxes :
- Liste Des postes disponibles (Liste of Available Careers
Opportunities)
- Formulaire de contact (contact form)
4. Latest blog articles
- Les derniers articles.
OTHER PAGES (to design once Homepage is approved)
- Varolinq (about us)
- Équipe (our team)
- Approche (our approach)
- Postes disponibles (Career opportunities)
- Publications (blog articles)
- Contact (Contact us)
Target Market(s)
ORGANIZATIONS:
Leaders of organizations seeking to recruit highly qualified staff.
HIGHLY QUALIFIED RESOURCES:
Senior individuals seeking a salary between $70,000 and $ $200,000 annually
PROFESSIONAL SECTORS:
manufacturing : Primary and secondary industries
pharmaceutical
Aerospace
Finances
Retail business
Engineering
Chemical and petrochemical
IT, telecommunications and high technology
Professional Organizations and Association
Industry/Entity Type
Business
Look and feel
Each slider illustrates characteristics of the customer's brand and the style your logo design should communicate.

```html
<!DOCTYPE html>
<html lang="fr">
<head>
<meta charset="utf-8">
<title>Varolinq – Recherche de cadres</title>
<link href="https://fonts.googleapis.com/css2?family=Raleway:wght@400;500;600&display=swap" rel="stylesheet">
<style>
:root{
  --ink:#333;
  --muted:#555;
  --teal-dark:#1c5762;
  --teal:#6fa4ae;
  --teal-light:#a9cbd1;
  --bar:#1f1f1f;
  --line:#dcdcdc;
  --foot:#e2e6e6;
  --white:#fff;
}
*{box-sizing:border-box;margin:0;padding:0}
html,body{width:1100px;height:1200px;overflow:hidden}
body{font-family:"Raleway",sans-serif;color:var(--ink);background:var(--white);position:relative}
h1,h2,h3{font-weight:400}
a{color:inherit;text-decoration:none}

.topbar{position:absolute;left:0;top:0;width:1100px;height:28px;background:var(--bar)}
.topbar-inner{position:absolute;right:176px;top:0;height:28px;display:flex;align-items:center;gap:15px;font-size:11.5px;color:var(--white)}
.topbar-sep{color:#999}
.social-squares{display:flex;gap:7px}
.social-square{width:18px;height:18px;border-radius:2px}
.social-square.one{background:#2c86c1}
.social-square.two{background:#f2f2f2}

.header{position:absolute;top:28px;left:0;width:1100px;height:80px}
.brand{position:absolute;left:168px;top:14px;display:flex;flex-direction:column;align-items:flex-start}
.brand-row{display:flex;align-items:center;gap:8px}
.brand-mark{width:12px;height:12px;background:#e0a21b}
.brand-name{font-size:25px;font-weight:500;color:var(--teal-dark);letter-spacing:1px}
.brand-tag{font-size:10.5px;color:#666;margin-left:60px;margin-top:1px}
.main-nav{position:absolute;right:175px;top:0;height:80px;display:flex}
.main-nav a{display:flex;align-items:center;padding:0 13px;font-size:11px;font-weight:500;border-left:1px solid #e4e4e4;text-transform:uppercase;padding-top:4px}
.main-nav a:first-child{border-left:none}
.main-nav a:last-child{padding-right:0}

.hero{position:absolute;top:108px;left:0;width:1100px;height:330px;background:linear-gradient(120deg,#8fb9c1 0%,#c2dadf 40%,#a9cbd1 62%,#76a9b3 100%);overflow:hidden;border-bottom:2px solid #5d8d96}
.hero-copy{position:absolute;right:709px;top:120px;text-align:right;color:var(--white);text-shadow:0 1px 3px rgba(0,0,0,.35)}
.hero-title{font-size:20px;font-weight:500}
.hero-sub{font-size:15px;line-height:18px;margin-top:6px}
.hero-link{display:inline-block;margin-top:8px;font-size:13px;color:#2a3c40;text-decoration:underline;text-shadow:none}
.hero-photo{position:absolute;left:460px;top:12px;width:380px;height:318px;background:radial-gradient(ellipse at 62% 50%,#7e8286 0%,rgba(111,116,120,.7) 40%,rgba(111,116,120,0) 72%)}

.slider-dots{position:absolute;left:510px;top:448px;width:75px;height:20px;border-radius:10px;background:#f6f6f6;box-shadow:0 2px 4px rgba(0,0,0,.2);display:flex;gap:5px;align-items:center;justify-content:center}
.slider-dots span{width:9px;height:9px;border-radius:50%;border:1px solid #bbb;background:#eee}
.slider-dots span.active{background:#7dbccb;border-color:#5aa}

.cta{position:absolute;top:497px;width:374px;height:168px;border:1px solid var(--line);padding:5px;background:var(--white)}
.cta.jobs{left:169px}
.cta.contact{left:553px}
.cta-inner{position:relative;width:100%;height:100%;background:linear-gradient(135deg,#9fc4cb 0%,#6fa3ad 100%);overflow:hidden}
.cta-photo{position:absolute;top:0;height:100%;width:190px}
.jobs .cta-photo{left:0;background:linear-gradient(90deg,#c8d6d8,#9cbfc5)}
.contact .cta-photo{right:0;background:linear-gradient(270deg,#e2d9d2,#9cbfc5)}
.cta-title{position:absolute;top:16px;font-size:17px;line-height:25px;color:var(--white);text-shadow:0 1px 2px rgba(0,0,0,.3)}
.jobs .cta-title{right:18px;text-align:right}
.contact .cta-title{left:17px}
.cta-link{position:absolute;bottom:18px;font-size:14px;color:var(--teal-dark);text-decoration:underline}
.jobs .cta-link{right:20px}
.contact .cta-link{left:17px}

.section-title{position:absolute;top:694px;left:169px;width:757px;display:flex;align-items:center;gap:12px;font-size:17px;color:#444}
.section-title::before,.section-title::after{content:"";flex:1;height:4px;border-top:1px dotted #bbb;border-bottom:1px dotted #bbb}

.article{position:absolute;width:374px;height:122px;border:1px solid var(--line);padding:5px;display:flex;gap:14px}
.article-photo{width:171px;height:110px;flex:none}
.photo-meeting{background:linear-gradient(90deg,#5c5c5c,#b8b8b8 60%,#dcdcdc)}
.photo-clock{background:linear-gradient(90deg,#c9c9c9,#eaeaea 70%,#d5d5d5)}
.article-body{padding-top:5px}
.article-title{font-size:13px;font-weight:500;color:var(--teal-dark)}
.article-text{font-size:10.5px;line-height:14.5px;color:var(--muted);margin-top:5px;width:175px}
.article-more{font-size:10.5px;color:#444;margin-top:6px;display:block}

.footer{position:absolute;top:1030px;left:0;width:1100px;height:125px;background:var(--foot)}
.footer-heading{position:absolute;top:18px;display:flex;align-items:center;gap:10px;font-size:13px;color:var(--teal-dark)}
.footer-heading::after{content:"";flex:1;border-top:1px dotted #999;border-bottom:1px dotted #999;height:4px}
.footer-heading.follow{left:170px;width:369px}
.footer-heading.news{left:554px;width:371px}
.social-block{position:absolute;top:54px;display:flex;gap:10px;font-size:10.5px;line-height:13px;color:#555}
.social-block.one{left:170px}
.social-block.two{left:326px}
.social-tile{width:48px;height:46px;border-radius:5px;flex:none}
.social-block.one .social-tile{background:#2d8ac4}
.social-block.two .social-tile{background:#f7f7f7;border:1px solid #ccc}
.contact-info{position:absolute;left:553px;top:50px;font-size:10.5px;line-height:16px;color:#444}

.bottom-bar{position:absolute;top:1155px;left:0;width:1100px;height:45px;background:var(--bar);border-top:2px solid #444;font-size:9.5px;color:#aaa}
.bottom-bar .copy{position:absolute;left:170px;top:16px}
.bottom-bar .credit{position:absolute;right:176px;top:16px}
</style>
</head>
<body>

<div class="topbar">
  <div class="topbar-inner">
    <a href="#">Accueil</a><a href="#">Plan du site</a><a href="#">Code d'éthique</a><a href="#">Contact</a><a href="#">English</a><span class="topbar-sep">|</span>
    <span class="social-squares" aria-hidden="true"><span class="social-square one"></span><span class="social-square two"></span></span>
  </div>
</div>

<header class="header">
  <a class="brand" href="#">
    <span class="brand-row"><span class="brand-mark"></span><span class="brand-name">VAROLINQ</span></span>
    <span class="brand-tag">Recherche de cadres</span>
  </a>
  <nav class="main-nav">
    <a href="#">A propos</a><a href="#">Équipe</a><a href="#">Approche</a><a href="#">Postes disponibles</a><a href="#">Publications</a>
  </nav>
</header>

<section class="hero">
  <div class="hero-copy">
    <h1 class="hero-title">Welcome to our site</h1>
    <p class="hero-sub">We are the leading Chasseurs de têtes<br>of quality individuals</p>
    <a class="hero-link" href="#">Know More &gt;</a>
  </div>
  <div class="hero-photo" role="img" aria-label="Photo of a businesswoman with arms crossed in front of a group of executives"></div>
</section>

<div class="slider-dots"><span class="active"></span><span></span><span></span><span></span></div>

<div class="cta jobs">
  <div class="cta-inner">
    <div class="cta-photo" role="img" aria-label="Photo of a smiling man reading a folder"></div>
    <h2 class="cta-title">Liste des postes<br>disponibles</h2>
    <a class="cta-link" href="#">Deatails &gt;</a>
  </div>
</div>
<div class="cta contact">
  <div class="cta-inner">
    <div class="cta-photo" role="img" aria-label="Photo of a smiling woman wearing a headset"></div>
    <h2 class="cta-title">Formulaire de<br>contact</h2>
    <a class="cta-link" href="#">Deatails &gt;</a>
  </div>
</div>

<h2 class="section-title">Les derniers articles</h2>

<article class="article" style="left:169px;top:735px">
  <div class="article-photo photo-meeting" role="img" aria-label="Photo of businessmen reviewing documents"></div>
  <div class="article-body"><h3 class="article-title">Article Headline</h3><p class="article-text">Lorem ipsum dolor sit amet, consectetur adipisicing elit, sed do eiusmod tempor incididunt ut labore et dolore magna aliqua.</p><a class="article-more" href="#">Read More &gt;</a></div>
</article>
<article class="article" style="left:552px;top:735px">
  <div class="article-photo photo-clock" role="img" aria-label="Photo of a businessman drawing a clock"></div>
  <div class="article-body"><h3 class="article-title">Article Headline</h3><p class="article-text">Lorem ipsum dolor sit amet, consectetur adipisicing elit, sed do eiusmod tempor incididunt ut labore et dolore magna aliqua.</p><a class="article-more" href="#">Read More &gt;</a></div>
</article>
<article class="article" style="left:169px;top:875px">
  <div class="article-photo photo-meeting" role="img" aria-label="Photo of businessmen reviewing documents"></div>
  <div class="article-body"><h3 class="article-title">Article Headline</h3><p class="article-text">Lorem ipsum dolor sit amet, consectetur adipisicing elit, sed do eiusmod tempor incididunt ut labore et dolore magna aliqua.</p><a class="article-more" href="#">Read More &gt;</a></div>
</article>
<article class="article" style="left:552px;top:875px">
  <div class="article-photo photo-clock" role="img" aria-label="Photo of a businessman drawing a clock"></div>
  <div class="article-body"><h3 class="article-title">Article Headline</h3><p class="article-text">Lorem ipsum dolor sit amet, consectetur adipisicing elit, sed do eiusmod tempor incididunt ut labore et dolore magna aliqua.</p><a class="article-more" href="#">Read More &gt;</a></div>
</article>

<footer class="footer">
  <h3 class="footer-heading follow">Suivez-nous sur Linkora</h3>
  <h3 class="footer-heading news">Inscrivez-vous à l'infolettre</h3>
  <div class="social-block one"><span class="social-tile"></span><span>Join us with<br>Linkora</span></div>
  <div class="social-block two"><span class="social-tile"></span><span>Present yourself with<br>Slidewell</span></div>
  <div class="contact-info">
    Corporqte Office : 57/A, Maple Row, CA &nbsp; Phone : 081 5520 - 1043<br>
    Registered Office : 17/B, Maple Row, CA &nbsp; Phone : 081 6631 - 2870<br>
    Support Email id : support.info@varolinq.co.in
  </div>
</footer>

<div class="bottom-bar">
  <span class="copy">© Varolinq - Tous droits réservés</span>
  <span class="credit">Site Web et stratégie Agence de Développement Internet</span>
</div>

</body>
</html>
```